Pillar Orchard
Professional
Mira Castellan, MBA
mira@pillarorchard.ca
www.pillarorchard.ca
Landscape layout. Please include tagline: "Building Momentum for Success"
Whatever you think will look good.

```html
<!DOCTYPE html>
<html lang="en">
<head>
<meta charset="utf-8">
<title>Pillar Orchard — Business Cards</title>
<link rel="stylesheet" href="https://fonts.googleapis.com/css2?family=Open+Sans:wght@400;600;700&family=Cinzel:wght@400&display=swap">
<style>
  :root {
    --sheet: #8c8c8c;
    --sheet-dark: #7d7d7d;
    --card-light: #ffffff;
    --card-dark: #2b2b2d;
    --navy: #0d1f5c;
    --royal: #1c3c9e;
    --accent: #2b5fb8;
    --silver: #c9ccd2;
    --ink: #2a2a2a;
    --muted: #6b6b6b;
    --muted-dark: #a9acb3;
    --label: #f2f2f2;
  }
  * { box-sizing: border-box; margin: 0; padding: 0; }
  html, body { width: 1200px; height: 806px; overflow: hidden; }
  body {
    background: radial-gradient(ellipse at center, var(--sheet) 0%, var(--sheet-dark) 100%);
    font-family: "Open Sans", Arial, sans-serif;
    position: relative;
  }
  .card {
    position: absolute;
    width: 504px;
    height: 288px;
    border-radius: 14px;
    overflow: hidden;
    box-shadow: 0 2px 6px rgba(0,0,0,.35);
  }
  .card--light { background: var(--card-light); color: var(--ink); }
  .card--dark { background: var(--card-dark); color: #f0f0f0; }
  .card svg.band { position: absolute; inset: 0; width: 504px; height: 288px; }

  .front-a { left: 67px; top: 41px; }
  .front-b { left: 638px; top: 41px; }
  .back-a { left: 67px; top: 422px; }
  .back-b { left: 638px; top: 422px; }

  .brand {
    position: absolute; left: 26px; top: 34px;
    display: flex; align-items: center; gap: 10px;
  }
  .brand-dot {
    width: 52px; height: 52px; border-radius: 50%;
    background: radial-gradient(circle at 40% 35%, var(--accent), var(--navy));
  }
  .brand-name {
    font-weight: 700; font-size: 27px; letter-spacing: .5px;
    text-transform: uppercase; line-height: 1;
  }
  .card--light .brand-name { color: var(--navy); }
  .card--dark .brand-name { color: #ffffff; }

  .tagline {
    position: absolute; left: 88px; top: 96px;
    font-size: 12px; font-weight: 400; letter-spacing: .6px;
  }
  .card--light .tagline { color: var(--muted); }
  .card--dark .tagline { color: var(--muted-dark); }

  .contact {
    position: absolute; left: 28px; bottom: 26px;
    list-style: none; font-size: 13px; line-height: 21px;
  }
  .contact li { display: flex; align-items: center; gap: 8px; }
  .contact svg { width: 12px; height: 12px; flex: none; }
  .card--light .contact { color: var(--ink); }
  .card--dark .contact { color: #ececec; }

  .holder {
    position: absolute; right: 30px; bottom: 28px;
    font-weight: 700; font-size: 16px; color: var(--accent);
  }

  .faint-disc {
    position: absolute; right: 40px; bottom: 20px;
    width: 130px; height: 130px; border-radius: 50%;
  }
  .card--light .faint-disc { background: rgba(0,0,0,.05); }
  .card--dark .faint-disc { background: rgba(255,255,255,.05); }

  .back-mark {
    position: absolute; left: 0; right: 0; top: 44px;
    display: flex; flex-direction: column; align-items: center;
  }
  .back-mark .brand-dot { width: 104px; height: 104px; margin-bottom: 12px; }
  .card--dark .back-mark .brand-dot {
    background: radial-gradient(circle at 40% 35%, var(--accent), var(--navy) 70%, #4a4d55);
  }
  .back-mark .brand-name { font-size: 18px; }
  .back-mark .tagline { position: static; margin-top: 8px; font-size: 11px; }
  .site {
    position: absolute; left: 0; right: 0; bottom: 36px;
    text-align: center; font-size: 11px; letter-spacing: 3px;
  }
  .card--light .site { color: var(--ink); }
  .card--dark .site { color: #e6e6e6; }

  .label {
    position: absolute; width: 504px; text-align: center;
    font-family: "Cinzel", "Times New Roman", serif;
    font-size: 19px; letter-spacing: 2px; color: var(--label);
  }
  .label--a { left: 67px; }
  .label--b { left: 638px; }
  .label--top { top: 348px; }
  .label--bottom { top: 738px; }
</style>
</head>
<body>

  <article class="card card--light front-a">
    <svg class="band" viewBox="0 0 504 288" aria-hidden="true">
      <path d="M150 0 H504 V150 C420 90 300 40 150 0 Z" fill="var(--silver)"/>
      <path d="M170 0 H504 V128 C420 70 310 28 170 0 Z" fill="var(--navy)"/>
      <path d="M260 0 H504 V100 C440 50 360 18 260 0 Z" fill="var(--royal)" opacity=".7"/>
    </svg>
    <div class="faint-disc"></div>
    <div class="brand"><span class="brand-dot"></span><span class="brand-name">Pillar Orchard</span></div>
    <p class="tagline">Building Momentum for Success</p>
    <ul class="contact">
      <li><svg viewBox="0 0 12 12"><path d="M3 1l2 2-1 1.5a7 7 0 0 0 3.5 3.5L9 7l2 2-1.5 2A9 9 0 0 1 1 2.5Z" fill="var(--accent)"/></svg>604-555-0182</li>
      <li><svg viewBox="0 0 12 12"><circle cx="6" cy="6" r="6" fill="var(--accent)"/><path d="M3 4h6v4H3z" fill="#fff"/></svg>mira@pillarorchard.ca</li>
      <li><svg viewBox="0 0 12 12"><circle cx="6" cy="6" r="5" fill="none" stroke="var(--accent)" stroke-width="1.4"/><path d="M1 6h10M6 1c-2 3-2 7 0 10M6 1c2 3 2 7 0 10" fill="none" stroke="var(--accent)"/></svg>www.pillarorchard.ca</li>
    </ul>
    <p class="holder">Mira Castellan, MBA</p>
  </article>

  <article class="card card--dark front-b">
    <svg class="band" viewBox="0 0 504 288" aria-hidden="true">
      <path d="M150 0 H504 V150 C420 90 300 40 150 0 Z" fill="#55585f"/>
      <path d="M170 0 H504 V128 C420 70 310 28 170 0 Z" fill="var(--navy)"/>
      <path d="M260 0 H504 V100 C440 50 360 18 260 0 Z" fill="var(--royal)" opacity=".7"/>
    </svg>
    <div class="faint-disc"></div>
    <div class="brand"><span class="brand-dot"></span><span class="brand-name">Pillar Orchard</span></div>
    <p class="tagline">Building Momentum for Success</p>
    <ul class="contact">
      <li><svg viewBox="0 0 12 12"><path d="M3 1l2 2-1 1.5a7 7 0 0 0 3.5 3.5L9 7l2 2-1.5 2A9 9 0 0 1 1 2.5Z" fill="var(--accent)"/></svg>604-555-0182</li>
      <li><svg viewBox="0 0 12 12"><circle cx="6" cy="6" r="6" fill="var(--accent)"/><path d="M3 4h6v4H3z" fill="#fff"/></svg>mira@pillarorchard.ca</li>
      <li><svg viewBox="0 0 12 12"><circle cx="6" cy="6" r="5" fill="none" stroke="var(--accent)" stroke-width="1.4"/><path d="M1 6h10M6 1c-2 3-2 7 0 10M6 1c2 3 2 7 0 10" fill="none" stroke="var(--accent)"/></svg>www.pillarorchard.ca</li>
    </ul>
    <p class="holder">Mira Castellan, MBA</p>
  </article>

  <p class="label label--a label--top">Business Card Front A</p>
  <p class="label label--b label--top">Business Card Front B</p>

  <article class="card card--light back-a">
    <div class="back-mark">
      <span class="brand-dot"></span>
      <span class="brand-name">Pillar Orchard</span>
      <p class="tagline">Building Momentum for Success</p>
    </div>
    <p class="site">www.pillarorchard.ca</p>
  </article>

  <article class="card card--dark back-b">
    <div class="back-mark">
      <span class="brand-dot"></span>
      <span class="brand-name">Pillar Orchard</span>
      <p class="tagline">Building Momentum for Success</p>
    </div>
    <p class="site">www.pillarorchard.ca</p>
  </article>

  <p class="label label--a label--bottom">Business Card Back A</p>
  <p class="label label--b label--bottom">Business Card Back B</p>

</body>
</html>
```